Contemporary Business card for Event Manager

Needed for my startup events company in Melbourne. Events I manage will be based within the fashion industry, sporting events, product launches etc. Not weddings or small dinner parties. Therfore I am after something professional and aimed at high end corporate market; but with the added emphasis on not being too conservative or boring. I am happy with a pop of colour e.g. yellow or copper foil.

Target Market(s)

fashion industry, design industry, high end sporting events e.g. Polo, Grand Prix, corporate clients,

Industry/Entity Type

Fashion

Contact Information for Business Card

side 1
Rosa Whitfield (can be upper or lower case, have a feature full stop between first and surname, or at the end of the nameetc) I am open to ideas. I would also be fine with my initials or name as a logo on the front (if this is the case my full name would need to go on the second side of the card.
2nd side:
Mobile: +61 455 718 263
email: rosa.whitfield@kestrelpost.com.au

on one side of the card:
event management | brand activation | Advisory Services

Font styles to use
Serif
Sans Serif

Requirements
Must have
• side 2 must have
• mobile number
• email address
• event management | brand activation | Advisory Services
• ** my full name (Rosa Whitfield) must be on the card somewhere)
Nice to have
• 1st side
• I see the card stock being either a dark grey, light grey, natural white or black (all matt colours on unprocessed card). I see the writing being copper foil, or foil white or foil black.
• To give you a feel for me, think: contemporary, minimalist, I love line drawings, concrete, white with grey vein marble, copper, white, grey, black...yes I do like colour....yellow (but pops of colour) ;) I would like the card to look designer but 'on trend' as I deal with a lot of design and fashion clients....styles - think the sophistication and simplicity of Lisoret or urban contemporary.
• some examples of what I like. Although please don't leet this limit you...I really am happy to have something a little more urban or design focused like a line drawing of an object, person too or a photo image too.
• https://www.pinvaultly.com/pin/837205164932850174/
• https://www.pinvaultly.com/pin/926318450173648205/
• https://www.pinvaultly.com/pin/318604927551203847/
• https://www.pinvaultly.com/pin/50938162477420916/
• https://www.pinvaultly.com/pin/41276039158862793/
• https://www.pinvaultly.com/pin/63098817524506139/
• https://www.pinvaultly.com/pin/704129583366208154/
• https://www.pinvaultly.com/pin/582046317729851460/
• https://www.pinvaultly.com/pin/467318205542097831/
Should not have
• should not look commercial or have cartoonish looking logos. However happy with a simple line drawing or logo with initials etc.

```html
<!DOCTYPE html>
<html lang="en">
<head>
<meta charset="utf-8">
<title>Rosa Whitfield — Business Card</title>
<link rel="stylesheet" href="https://fonts.googleapis.com/css2?family=Source+Sans+3:wght@400&display=swap">
<style>
  :root {
    --backdrop: #cfcfcf;
    --card-stock: #050505;
    --copper: #c08a5c;
    --copper-light: #e6b78c;
    --copper-dark: #7a4a2a;
  }

  * { margin: 0; padding: 0; box-sizing: border-box; }

  html, body {
    width: 1200px;
    height: 676px;
    overflow: hidden;
  }

  body {
    background: var(--backdrop);
    font-family: "Source Sans 3", "Myriad Pro", Arial, sans-serif;
    position: relative;
  }

  .business-card {
    position: absolute;
    left: 150px;
    top: 63px;
    width: 900px;
    height: 550px;
    background: var(--card-stock);
    color: var(--copper);
    text-align: center;
  }

  .monogram {
    position: absolute;
    top: 70px;
    left: 0;
    width: 100%;
    display: flex;
    justify-content: center;
  }

  .monogram-text {
    font-size: 108px;
    line-height: 1;
    font-weight: 400;
    color: var(--copper);
    letter-spacing: -2px;
  }

  .card-name {
    position: absolute;
    top: 200px;
    left: 0;
    width: 100%;
    font-size: 66px;
    font-weight: 400;
    line-height: 1;
    letter-spacing: 0.5px;
  }

  .contact-details {
    position: absolute;
    top: 305px;
    left: 0;
    width: 100%;
    list-style: none;
    font-size: 22px;
    line-height: 30px;
  }

  .services {
    position: absolute;
    left: 52px;
    right: 52px;
    top: 425px;
  }

  .services-list {
    display: flex;
    justify-content: space-between;
    font-size: 26px;
    line-height: 1;
    padding: 0 12px 10px;
  }

  .services-divider {
    color: var(--copper-light);
  }

  .services-rule {
    display: block;
    width: 100%;
    height: 3px;
  }
</style>
</head>
<body>
  <article class="business-card">
    <div class="monogram">
      <span class="monogram-text">RW</span>
    </div>

    <h1 class="card-name">Rosa Whitfield</h1>

    <ul class="contact-details">
      <li class="contact-mobile">Mobile: +61 455 718 263</li>
      <li class="contact-email">email: rosa.whitfield@kestrelpost.com.au</li>
    </ul>

    <div class="services">
      <p class="services-list">
        <span>Event Management</span>
        <span class="services-divider">|</span>
        <span>Brand Activation</span>
        <span class="services-divider">|</span>
        <span>Advisory Services</span>
      </p>
      <svg class="services-rule" viewBox="0 0 796 3" preserveAspectRatio="none" aria-hidden="true">
        <defs>
          <linearGradient id="copper-foil" x1="0" x2="1" y1="0" y2="0">
            <stop offset="0" stop-color="#7a4a2a"/>
            <stop offset="0.35" stop-color="#e6b78c"/>
            <stop offset="0.65" stop-color="#c08a5c"/>
            <stop offset="1" stop-color="#7a4a2a"/>
          </linearGradient>
        </defs>
        <rect x="0" y="0" width="796" height="3" fill="url(#copper-foil)"/>
      </svg>
    </div>
  </article>
</body>
</html>
```